Zephyr Quill - Dog Supplement Brand

Here a link to a word doc with all of my info.
Please read it carefully.
https://files.brindlemoor.net/page/d/7tRkWpLzQ2mNvA84xHcYbEuJ0sFdKo93Tg5LhPq-2/view?ref=open
Its 2 pages. Home Page and Product Page.
Oh and btw: the poses I attached dont have a shadow, so it would be good if you added a shadow to the poses .
If you have any questions please let me know.
Target Market(s)
Dog Owners In UK
Industry/Entity Type
Dog supplements
Number of Pages Required
2 page
Requirements
Must have
- Home page and product page files. Super Hero Theme.

```html
<!DOCTYPE html>
<html lang="en">
<head>
<meta charset="utf-8">
<title>Zephyr Quill – Home</title>
<link href="https://fonts.googleapis.com/css2?family=Poppins:wght@400;500;600;700;800;900&display=swap" rel="stylesheet">
<style>
:root{
  --red:#e8232a;
  --red-deep:#c9161d;
  --ink:#111111;
  --text:#2b2b2b;
  --muted:#777777;
  --grey-bg:#f4f4f4;
  --white:#ffffff;
  --green:#1fc24a;
  --yellow:#f2c21b;
  --purple:#8a22e0;
  --orange:#c4520f;
  --star:#f5a623;
}
*{box-sizing:border-box;margin:0;padding:0}
html,body{width:1200px;height:5098px;overflow:hidden}
body{font-family:'Poppins',sans-serif;color:var(--text);background:var(--white);position:relative}
section,header,footer,.announce{position:absolute;left:0;width:1200px}
.abs{position:absolute}
.ph{position:absolute;border-radius:24px}

/* announcement */
.announce{top:0;height:34px;background:var(--red);color:#fff;font-size:11px;font-weight:500;text-align:center;line-height:34px}

/* header */
.site-header{top:34px;height:77px;background:#fff;border-bottom:1px solid #eee}
.brand{position:absolute;left:0;width:1200px;top:24px;text-align:center;font-weight:800;font-size:22px;color:var(--ink)}
.hdr-icon{position:absolute;top:28px}

/* hero */
.hero{top:111px;height:564px;background:radial-gradient(circle at 70% 45%,#f0474d 0%,var(--red) 45%,var(--red-deep) 100%)}
.hero-kicker{left:100px;top:156px;font-size:27px;color:#fff;font-weight:400}
.hero-title{left:100px;top:188px;font-size:70px;font-weight:800;color:#fff;line-height:1}
.hero-sub{left:100px;top:268px;font-size:26px;color:#fff;font-weight:400}
.hero-line{left:462px;top:290px;width:140px;height:2px;background:rgba(255,255,255,.7)}
.hero-hero{left:100px;top:300px;font-size:82px;font-weight:800;color:#fff;line-height:1.1}
.hero-art{left:670px;top:60px;width:340px;height:340px;border-radius:50%;background:radial-gradient(circle,#f4f4f4 0%,#cfcfcf 55%,rgba(200,30,30,0) 72%)}

/* about */
.about{top:675px;height:675px;background:#fff}
.about-art{left:120px;top:70px;width:350px;height:560px;background:linear-gradient(180deg,#e9e9e9,#cfcfcf)}
.about-hi{left:538px;top:170px;font-size:50px;font-weight:800;color:var(--ink)}
.about-name{left:538px;top:228px;font-size:64px;font-weight:800;color:var(--red);line-height:1.1}
.body-copy{font-size:17px;line-height:33px;color:var(--text)}
.about-copy{left:540px;top:330px;width:530px}
.btn{position:absolute;background:var(--red);color:#fff;font-weight:500;border-radius:8px;text-align:center}
.about-btn{left:540px;top:530px;width:248px;height:52px;line-height:52px;font-size:16px}

/* offer */
.offer{top:1350px;height:674px;background:var(--grey-bg)}
.mascot-sm{left:540px;width:120px;height:115px;border-radius:50%;background:radial-gradient(circle,#dcdcdc 0%,#bdbdbd 60%,rgba(0,0,0,0) 72%)}
.section-title{left:0;width:1200px;text-align:center;font-size:50px;font-weight:800;color:var(--ink)}
.section-title .hl,.hl{color:var(--red)}
.card{position:absolute;width:236px;height:140px;background:#fff;border:4px solid var(--c);border-radius:22px;text-align:center;display:flex;flex-direction:column;justify-content:center}
.card::after{content:"";position:absolute;left:14px;top:14px;width:236px;height:140px;border-radius:22px;z-index:-1;background-image:radial-gradient(#333 1.6px,transparent 1.8px);background-size:8px 8px}
.card .ct{font-size:20px;font-weight:700;color:var(--c)}
.card .cs{font-size:20px;font-weight:400;color:var(--c)}
.card-wrap{position:absolute;left:0;top:0;width:1200px;height:674px;isolation:isolate}

/* vets */
.vets{top:2024px;height:676px;background:#fff}
.vets-art{left:90px;top:70px;width:330px;height:520px;background:linear-gradient(180deg,#ececec,#cdcdcd)}
.vets-title{left:430px;top:80px;font-size:43px;font-weight:800;color:var(--ink)}
.video-frame{left:428px;top:145px;width:672px;height:388px;border-radius:14px;background:#e7e7e7;padding:8px}
.video{width:100%;height:100%;border-radius:10px;background:#000;position:relative}

/* testimonials */
.love{top:2700px;height:674px;background:var(--grey-bg)}
.t-card{position:absolute;top:255px;width:320px;height:350px;background:#fff;border-radius:8px;text-align:center}
.avatar{position:absolute;left:124px;top:42px;width:72px;height:72px;border-radius:50%;background:radial-gradient(circle,#f1c9a5,#d6925c)}
.t-name{position:absolute;left:0;width:320px;top:130px;font-size:19px;font-weight:600;color:var(--ink)}
.t-stars{position:absolute;left:120px;top:163px}
.t-date{position:absolute;left:0;width:320px;top:188px;font-size:13px;color:var(--muted)}
.t-rule{position:absolute;top:228px;height:1px;width:90px;background:#bbb}
.t-dot{position:absolute;left:150px;top:221px;width:14px;height:14px;border:1.5px solid #999;transform:rotate(45deg)}
.t-text{position:absolute;left:40px;width:240px;top:258px;font-size:13px;line-height:21px;color:var(--muted)}

/* regulated */
.regulated{top:3374px;height:675px;background:#fff}
.badge{position:absolute;top:78px;width:96px;height:96px;border-radius:50%;border:3px solid #333;background:#fff}
.reg-title{left:100px;top:212px;font-size:48px;font-weight:800;color:var(--ink);line-height:1.1}
.reg-title2{left:100px;top:268px;font-size:66px;font-weight:800;color:var(--red);line-height:1.1}
.reg-copy{left:100px;top:370px;width:530px}
.reg-art{left:660px;top:60px;width:370px;height:560px;background:linear-gradient(180deg,#eeeeee,#cfcfcf)}

/* why */
.why{top:4049px;height:673px;background:#fff}
.why-art{left:200px;top:100px;width:235px;height:540px;background:linear-gradient(180deg,#ebebeb,#cccccc)}
.why-title{left:540px;top:132px;font-size:48px;font-weight:800;color:var(--ink)}
.why-list{position:absolute;left:545px;top:210px;list-style:none}
.why-list li{height:42px;display:flex;align-items:center;font-size:15px;color:var(--text)}
.why-list svg{margin-right:16px;flex:none}

/* cta */
.cta{top:4722px;height:222px;background:linear-gradient(180deg,#fff 0%,#ececec 35%,#e8e8e8 100%)}
.cta-title{left:0;width:1200px;top:106px;text-align:center;font-size:35px;font-weight:700;color:var(--ink)}
.cta-btn{left:525px;top:175px;width:150px;height:44px;line-height:44px;font-size:14px}

/* footer */
.site-footer{top:4944px;height:154px;background:#fff;border-top:1px solid #eee}
.f-label{left:44px;top:30px;font-size:12px;color:var(--muted)}
.f-select{left:44px;top:52px;width:196px;height:36px;border:1px solid #999;border-radius:3px;font-size:12px;line-height:34px;padding-left:14px;color:var(--text)}
.pay{position:absolute;top:60px;width:34px;height:22px;border-radius:3px;border:1px solid #ccc}
.f-copy{right:44px;top:96px;font-size:10px;color:var(--muted)}
</style>
</head>
<body>

<div class="announce">FREE Shipping on all orders over £20 +++ Get your first bottle for just £10 when you join forces!</div>

<header class="site-header">
  <svg class="hdr-icon" style="left:44px" width="20" height="20" viewBox="0 0 20 20"><path d="M2 5h16M2 10h16M2 15h16" stroke="#222" stroke-width="1.6"/></svg>
  <div class="brand">Zephyr Quill</div>
  <svg class="hdr-icon" style="left:1060px" width="20" height="20" viewBox="0 0 20 20"><circle cx="8.5" cy="8.5" r="5.5" fill="none" stroke="#222" stroke-width="1.6"/><path d="M12.5 12.5l5 5" stroke="#222" stroke-width="1.6"/></svg>
  <svg class="hdr-icon" style="left:1098px" width="20" height="20" viewBox="0 0 20 20"><circle cx="10" cy="7" r="3.5" fill="none" stroke="#222" stroke-width="1.6"/><path d="M3 18c1-4 4-6 7-6s6 2 7 6" fill="none" stroke="#222" stroke-width="1.6"/></svg>
  <svg class="hdr-icon" style="left:1136px" width="20" height="20" viewBox="0 0 20 20"><path d="M3 6h14l-1 12H4z" fill="none" stroke="#222" stroke-width="1.6"/><path d="M7 6V4a3 3 0 0 1 6 0v2" fill="none" stroke="#222" stroke-width="1.6"/></svg>
</header>

<section class="hero">
  <div class="abs hero-kicker">Join Forces with</div>
  <div class="abs hero-title">ZEPHYR QUILL</div>
  <div class="abs hero-sub">&amp; Let him be your beloved</div>
  <div class="abs hero-line"></div>
  <div class="abs hero-hero">Dog's HERO!</div>
  <div class="ph hero-art" role="img" aria-label="3D husky superhero mascot flying with red cape"></div>
</section>

<section class="about">
  <div class="ph about-art" role="img" aria-label="Husky superhero mascot waving, wearing red cape and gold belt"></div>
  <div class="abs about-hi">HI! I'm</div>
  <div class="abs about-name">ZEPHYR QUILL!</div>
  <p class="abs body-copy about-copy">Lorem ipsum dolor sit amet, consectetur adipisicing elit, sed do eiusmod tempor incididunt ut labore et dolore magna aliqua. Ut enim ad minim veniam, quis nostrud exercitation ullamco laboris nisi ut aliquip ex ea commodo consequat...</p>
  <div class="btn about-btn">Read more about me!</div>
</section>

<section class="offer">
  <div class="ph mascot-sm" style="top:25px" role="img" aria-label="Small husky mascot peeking over heading"></div>
  <h2 class="abs section-title" style="top:140px">HERE'S WHAT <span class="hl">I OFFER</span></h2>
  <div class="card-wrap">
    <div class="card" style="left:190px;top:235px;--c:var(--ink)"><div class="ct">ZEPHYR QUILL</div><div class="cs">Calm</div></div>
    <div class="card" style="left:478px;top:240px;--c:var(--red)"><div class="ct">ZEPHYR QUILL</div><div class="cs">Joint Support</div></div>
    <div class="card" style="left:766px;top:240px;--c:var(--green)"><div class="ct">ZEPHYR QUILL</div><div class="cs">MultiVits</div></div>
    <div class="card" style="left:190px;top:445px;--c:var(--yellow)"><div class="ct">ZEPHYR QUILL</div><div class="cs">Omega 369</div></div>
    <div class="card" style="left:478px;top:450px;--c:var(--purple)"><div class="ct">ZEPHYR QUILL</div><div class="cs">Probiotics</div></div>
    <div class="card" style="left:766px;top:445px;--c:var(--orange)"><div class="ct">ZEPHYR QUILL</div><div class="cs">Digestive Support</div></div>
  </div>
</section>

<section class="vets">
  <div class="ph vets-art" role="img" aria-label="Husky mascot flexing muscles with red cape"></div>
  <h2 class="abs vets-title">APPROVED BY EXPERT <span class="hl">VETS</span></h2>
  <div class="abs video-frame">
    <div class="video" role="img" aria-label="Video of vets approving the supplements">
      <svg style="position:absolute;left:314px;top:168px" width="36" height="36" viewBox="0 0 36 36"><circle cx="18" cy="18" r="17" fill="#555"/><path d="M14 11l11 7-11 7z" fill="#ddd"/></svg>
    </div>
  </div>
</section>

<section class="love">
  <div class="ph mascot-sm" style="top:30px" role="img" aria-label="Small husky mascot peeking over heading"></div>
  <h2 class="abs section-title" style="top:150px">PEOPLE <span class="hl">LOVE ME</span></h2>

  <div class="t-card" style="left:100px">
    <div class="avatar" role="img" aria-label="Customer portrait"></div>
    <div class="t-name">Mira Tolvane</div>
    <svg class="t-stars" width="80" height="14" viewBox="0 0 80 14"><g fill="var(--star)"><path id="s" d="M7 0l2 4.6 5 .5-3.8 3.3 1.1 4.9L7 10.8 2.7 13.3l1.1-4.9L0 5.1l5-.5z"/><use href="#s" x="16"/><use href="#s" x="32"/><use href="#s" x="48"/><use href="#s" x="64"/></g></svg>
    <div class="t-date">January 11, 2022</div>
    <div class="t-rule" style="left:48px"></div><div class="t-dot"></div><div class="t-rule" style="left:182px"></div>
    <p class="t-text">Use this text to share information about your brand with your customers.</p>
  </div>
  <div class="t-card" style="left:440px">
    <div class="avatar" role="img" aria-label="Customer portrait"></div>
    <div class="t-name">Mira Tolvane</div>
    <svg class="t-stars" width="80" height="14" viewBox="0 0 80 14"><g fill="var(--star)"><use href="#s"/><use href="#s" x="16"/><use href="#s" x="32"/><use href="#s" x="48"/><use href="#s" x="64"/></g></svg>
    <div class="t-date">January 11, 2022</div>
    <div class="t-rule" style="left:48px"></div><div class="t-dot"></div><div class="t-rule" style="left:182px"></div>
    <p class="t-text">Use this text to share information about your brand with your customers.</p>
  </div>
  <div class="t-card" style="left:780px">
    <div class="avatar" role="img" aria-label="Customer portrait"></div>
    <div class="t-name">Mira Tolvane</div>
    <svg class="t-stars" width="80" height="14" viewBox="0 0 80 14"><g fill="var(--star)"><use href="#s"/><use href="#s" x="16"/><use href="#s" x="32"/><use href="#s" x="48"/><use href="#s" x="64"/></g></svg>
    <div class="t-date">January 11, 2022</div>
    <div class="t-rule" style="left:48px"></div><div class="t-dot"></div><div class="t-rule" style="left:182px"></div>
    <p class="t-text">Use this text to share information about your brand with your customers.</p>
  </div>
</section>

<section class="regulated">
  <div class="badge" style="left:100px" role="img" aria-label="Quality certification badge"></div>
  <div class="badge" style="left:238px;border-color:#1b8a2e" role="img" aria-label="Manufacturing standard badge"></div>
  <div class="badge" style="left:376px" role="img" aria-label="Guarantee badge"></div>
  <h2 class="abs reg-title">REGULATED &amp;</h2>
  <h2 class="abs reg-title2">CERTIFIED</h2>
  <p class="abs body-copy reg-copy">Lorem ipsum dolor sit amet, consectetur adipisicing elit, sed do eiusmod tempor incididunt ut labore et dolore magna aliqua. Ut enim ad minim veniam, quis nostrud exercitation ullamco laboris nisi ut aliquip ex ea commodo consequat. Duis aute irure dolor in reprehenderit in voluptate velit esse cillum dolore eu fugiat nulla pariatur.</p>
  <div class="ph reg-art" role="img" aria-label="Husky mascot in lab coat and goggles holding test tubes"></div>
</section>

<section class="why">
  <div class="ph why-art" role="img" aria-label="Husky mascot standing with arms crossed and red cape"></div>
  <h2 class="abs why-title">WHY CHOOSE <span class="hl">ME?</span></h2>
  <ul class="why-list">
    <li><svg width="16" height="16" viewBox="0 0 16 16"><path d="M2 8.5l4 4 8-9" fill="none" stroke="#555" stroke-width="1.8"/></svg>Only Organic &amp; Natural Ingredients</li>
    <li><svg width="16" height="16" viewBox="0 0 16 16"><path d="M2 8.5l4 4 8-9" fill="none" stroke="#555" stroke-width="1.8"/></svg>20% OFF For All Zephyr Quill Squad Members</li>
    <li><svg width="16" height="16" viewBox="0 0 16 16"><path d="M2 8.5l4 4 8-9" fill="none" stroke="#555" stroke-width="1.8"/></svg>Free Next Day UK Delivery</li>
    <li><svg width="16" height="16" viewBox="0 0 16 16"><path d="M2 8.5l4 4 8-9" fill="none" stroke="#555" stroke-width="1.8"/></svg>Regulated and Certified</li>
    <li><svg width="16" height="16" viewBox="0 0 16 16"><path d="M2 8.5l4 4 8-9" fill="none" stroke="#555" stroke-width="1.8"/></svg>10% Charity Donation</li>
    <li><svg width="16" height="16" viewBox="0 0 16 16"><path d="M2 8.5l4 4 8-9" fill="none" stroke="#555" stroke-width="1.8"/></svg>Approved By Vets</li>
    <li><svg width="16" height="16" viewBox="0 0 16 16"><path d="M2 8.5l4 4 8-9" fill="none" stroke="#555" stroke-width="1.8"/></svg>24/7 Customer Support</li>
    <li><svg width="16" height="16" viewBox="0 0 16 16"><path d="M2 8.5l4 4 8-9" fill="none" stroke="#555" stroke-width="1.8"/></svg>30 Days, 100% Money Back Guarantee</li>
    <li><svg width="16" height="16" viewBox="0 0 16 16"><path d="M2 8.5l4 4 8-9" fill="none" stroke="#555" stroke-width="1.8"/></svg>Safe &amp; Secure Payments</li>
  </ul>
</section>

<section class="cta">
  <div class="ph mascot-sm" style="top:-18px;width:150px;left:525px;height:125px" role="img" aria-label="Husky mascot flying forward"></div>
  <h2 class="abs cta-title">So how about you give it a try?</h2>
  <div class="btn cta-btn">JOIN FORCES!</div>
</section>

<footer class="site-footer">
  <div class="abs f-label">Country/region</div>
  <div class="abs f-select">United Kingdom (GBP £) &nbsp;⌄</div>
  <div class="pay" style="left:742px;background:#2e77bc"></div>
  <div class="pay" style="left:784px;background:#fff"></div>
  <div class="pay" style="left:826px;background:#fff"></div>
  <div class="pay" style="left:868px;background:#fff"></div>
  <div class="pay" style="left:910px;background:#fff"></div>
  <div class="pay" style="left:952px;background:#fff"></div>
  <div class="pay" style="left:994px;background:#fff"></div>
  <div class="pay" style="left:1036px;background:#fff"></div>
  <div class="pay" style="left:1078px;background:#5a31f4"></div>
  <div class="pay" style="left:1120px;background:#fff"></div>
  <div class="abs f-copy">© 2022, Zephyr Quill UK</div>
</footer>

</body>
</html>
```